Kornfeldtakt.de

The ostwind-tauschhalle.de (oth) is an internet portal for the incurance industry in Germany: www.ostwind-tauschhalle.de.

We are now planning to start a new brand Kornfeldtakt.de, which will be integral part of oth, but will have own logo, navigation etc. The main topic of Kornfeldtakt.de will be the new digital way of communication between insurance companies and insurance brokers (selling companies' products).

The main content of Kornfeldtakt.de will consist of articles / blog entries and at this moment we would like to concentrate on that part of our new brand.

At the top of the page we will always have a cover story, which will be the latest published article.

Under the cover story the user will find other articles. The articles should have variable widths (1/3, 2/3, 3/3). We will also need some additional elements like newsletter subscription, articles with most clicks etc.

Please use as reference this page:
https://www.brenntal.de/

We really like how it is designed.

Here you will find the current state of our project:

https://relaunch.ostwind-tauschhalle.de/kornfeldtakt

We will also need a logo for Kornfeldtakt.de, which should include the subtitle: Stets eigenständig, nie beliebig AND powerd by ostwind-tauschhalle.de

Due to the problems with the "Pool" functionality at Formbazaar we will need more time to verify your projects in our teem - but we are on it.

```html
<!DOCTYPE html>
<html lang="en">
<head>
<meta charset="utf-8">
<title>Kornfeldtakt</title>
<link rel="stylesheet" href="https://fonts.googleapis.com/css2?family=Lato:wght@400;700;900&family=Montserrat:wght@500;700;800&display=swap">
<style>
:root{
  --red:#f0363f;
  --blue:#2d6a9b;
  --ink:#1d1d1d;
  --text:#3a3a3a;
  --grey-bg:#efefef;
  --footer:#1f1f1f;
  --white:#fff;
}
*{box-sizing:border-box;margin:0;padding:0}
html,body{width:1200px;height:3333px;overflow:hidden}
body{font-family:"Lato",sans-serif;color:var(--ink);background:var(--white);position:relative}
.wrap{width:940px;margin:0 auto;position:relative}
a{color:inherit;text-decoration:none}

/* header */
.site-header{height:103px;position:relative}
.brand{position:absolute;left:130px;top:26px;display:flex;align-items:center;gap:14px}
.brand-square{width:56px;height:56px;background:var(--blue)}
.brand-name{font-family:"Montserrat",sans-serif;font-weight:500;font-size:29px;line-height:32px;color:var(--ink)}
.brand-tag{font-size:13px;color:var(--text);margin-top:4px}
.search{position:absolute;left:739px;top:20px;width:170px;height:32px;border:1px solid #999;font-size:11px;color:#777;padding:8px 10px}
.search svg{position:absolute;right:8px;top:9px}
.btn-subscribe{position:absolute;left:957px;top:20px;width:111px;height:32px;background:var(--red);color:#fff;font-size:14px;display:flex;align-items:center;justify-content:center;gap:6px}
.main-nav{position:absolute;right:132px;top:70px;display:flex;gap:34px;font-size:16px}
.main-nav .active{color:var(--red);text-decoration:underline}

/* hero */
.hero{height:467px;position:relative;background:linear-gradient(100deg,#6e6558 0%,#a89a86 30%,#c9bca6 50%,#8e8372 70%,#4a4b55 100%);text-align:center}
.hero::after{content:"";position:absolute;inset:0;background:rgba(0,0,0,.15)}
.hero-inner{position:relative;z-index:1;padding-top:60px}
.hero h1{font-family:"Montserrat",sans-serif;font-weight:800;font-size:27px;line-height:34px;color:#fff;text-transform:uppercase;text-shadow:0 2px 4px rgba(0,0,0,.45)}
.btn-hero{display:inline-block;margin-top:24px;background:var(--red);color:#fff;font-size:16px;padding:12px 20px}
.dots{position:absolute;left:0;right:0;bottom:32px;z-index:1;display:flex;justify-content:center;gap:6px}
.dots span{width:8px;height:8px;background:#fff}
.dots .on{background:var(--red);outline:2px solid #fff}

/* section titles */
.section-title{font-family:"Montserrat",sans-serif;font-weight:700;font-size:19px;text-align:center;text-transform:uppercase}
.section-title::after{content:"";display:block;width:52px;height:3px;background:#555;margin:16px auto 0}

/* latest published */
.latest{height:413px;padding-top:46px}
.latest-row{display:flex;gap:12px;margin-top:34px}
.feature-card{width:226px;height:230px;position:relative;border-radius:8px;overflow:hidden}
.feature-card .ph{position:absolute;inset:0}
.feature-card .caption{position:absolute;left:14px;right:14px;bottom:0;height:65px;background:#fff;border-radius:10px 10px 0 0;padding:12px 18px}
.caption .date{font-size:11px;color:var(--text)}
.caption .title{font-size:13px;line-height:17px;margin-top:5px}

/* articles */
.articles{background:var(--grey-bg);height:1348px;padding-top:44px}
.grid{display:grid;grid-template-columns:repeat(3,300px);column-gap:19px;row-gap:20px;margin-top:32px}
.article-card{background:#fff;border-radius:10px;overflow:hidden;height:381px}
.article-card .ph{height:173px}
.card-body{padding:24px 24px}
.date{font-size:11px;color:var(--text)}
.card-title{font-weight:400;font-size:14px;line-height:18px;margin-top:8px}
.card-text{font-size:12px;line-height:17.5px;color:var(--text);margin-top:12px}
.btn-pill{display:inline-block;background:var(--red);color:#fff;font-size:11px;padding:7px 12px;border-radius:16px;margin-top:18px}

/* newsletter */
.newsletter{background:var(--blue);height:168px;color:#fff;position:relative}
.newsletter h2{position:absolute;left:134px;top:40px;font-family:"Montserrat",sans-serif;font-weight:800;font-size:25px}
.newsletter p{position:absolute;left:135px;top:84px;width:370px;font-size:13px;line-height:18px;color:#dfe8f1}
.nl-form{position:absolute;left:594px;top:48px;width:465px;height:65px;background:#fff;border-radius:33px;display:flex;align-items:center;padding-left:28px;color:#333;font-size:14px;gap:12px}
.nl-form .btn{position:absolute;right:18px;top:13px;background:var(--red);color:#fff;font-family:"Montserrat",sans-serif;font-weight:700;font-size:14px;padding:11px 16px;border-radius:20px}

/* blog */
.blog{height:621px;padding-top:58px}
.blog-row{display:flex;gap:27px;margin-top:32px}
.blog-main{width:453px;position:relative;height:450px}
.blog-main .ph{height:259px;border-radius:8px}
.blog-main h3{font-weight:400;font-size:17px;line-height:22px;margin-top:30px}
.blog-main .card-text{margin-top:16px}
.blog-small{width:218px;position:relative;height:450px}
.blog-small .ph{height:156px;border-radius:8px}
.blog-small h3{font-weight:400;font-size:14px;line-height:17px;margin-top:30px}
.blog-small .card-text{margin-top:18px}
.blog-main .btn-pill,.blog-small .btn-pill{position:absolute;top:415px;left:0;margin-top:0}

/* footer */
.site-footer{background:var(--footer);height:213px;color:#fff;position:relative}
.site-footer .brand{top:40px}
.site-footer .brand-name,.site-footer .brand-tag{color:#fff}
.follow{position:absolute;right:130px;top:36px;display:flex;align-items:center;gap:14px;font-size:12px}
.follow span.icon{width:16px;height:16px;border-radius:50%;border:2px solid #fff}
.foot-nav{position:absolute;right:132px;top:90px;display:flex;gap:34px;font-size:16px}
.foot-rule{position:absolute;left:130px;right:132px;top:131px;height:2px;background:#444}
.copyright{position:absolute;left:130px;top:170px;font-size:12px}
.powered{position:absolute;right:132px;top:158px;display:flex;align-items:center;gap:10px;font-size:12px}
.powered .mark{width:34px;height:34px;background:var(--red)}
.powered .name{font-size:13px;line-height:16px}
</style>
</head>
<body>

<header class="site-header">
  <div class="brand">
    <div class="brand-square"></div>
    <div><div class="brand-name">Kornfeldtakt</div><div class="brand-tag">Stets eigenständig, nie beliebig</div></div>
  </div>
  <div class="search">Search
    <svg width="12" height="12" viewBox="0 0 12 12"><circle cx="5" cy="5" r="3.8" fill="none" stroke="#555" stroke-width="1.4"/><line x1="8" y1="8" x2="11" y2="11" stroke="#555" stroke-width="1.4"/></svg>
  </div>
  <a class="btn-subscribe" href="#"><svg width="12" height="9" viewBox="0 0 12 9"><rect width="12" height="9" fill="#fff"/><path d="M0 0l6 5 6-5" fill="none" stroke="#f0363f" stroke-width="1.2"/></svg>Subscribe</a>
  <nav class="main-nav"><a class="active" href="#">Home</a><a href="#">About Us</a><a href="#">Blog</a><a href="#">Articles</a><a href="#">Contact</a></nav>
</header>

<section class="hero" role="img" aria-label="Photo of an insurance broker and client signing a contract at a desk">
  <div class="hero-inner">
    <h1>The new digital way of communication<br>between insurance companies and<br>insurance brokers</h1>
    <a class="btn-hero" href="#">Read More</a>
  </div>
  <div class="dots"><span></span><span></span><span class="on"></span><span></span><span></span></div>
</section>

<section class="latest">
  <h2 class="section-title">Latest Published Article</h2>
  <div class="wrap latest-row">
    <article class="feature-card"><div class="ph" role="img" aria-label="Photo of hands passing a document" style="background:linear-gradient(135deg,#2e3b58,#c9ccd4 60%,#eef0f2)"></div><div class="caption"><div class="date">Feb 22, 2022</div><div class="title">Lorem Ipsum is simply dummy text of the</div></div></article>
    <article class="feature-card"><div class="ph" role="img" aria-label="Photo of an insurance form on a clipboard" style="background:linear-gradient(160deg,#e6e1da,#bfb5a8 60%,#8d8378)"></div><div class="caption"><div class="date">Feb 22, 2022</div><div class="title">Lorem Ipsum is simply dummy text of the</div></div></article>
    <article class="feature-card"><div class="ph" role="img" aria-label="Photo of a business handshake in an office" style="background:linear-gradient(120deg,#4d5a3e,#c7c2b8 50%,#3d4150)"></div><div class="caption"><div class="date">Feb 22, 2022</div><div class="title">Lorem Ipsum is simply dummy text of the</div></div></article>
    <article class="feature-card"><div class="ph" role="img" aria-label="Photo of a couple meeting an advisor" style="background:linear-gradient(120deg,#d9d4cc,#9a8a78 50%,#e4dfd6)"></div><div class="caption"><div class="date">Feb 22, 2022</div><div class="title">Lorem Ipsum is simply dummy text of the</div></div></article>
  </div>
</section>

<section class="articles">
  <h2 class="section-title">Articles</h2>
  <div class="wrap grid">
    <article class="article-card"><div class="ph" role="img" aria-label="Photo of a meeting behind a glass door" style="background:linear-gradient(90deg,#e8e6e2,#c9b9a4 50%,#8a5a36)"></div><div class="card-body"><div class="date">Feb 22, 2022</div><h3 class="card-title">There are many variations of passages of Lorem Ipsum available</h3><p class="card-text">Sed ut perspiciatis unde omnis iste natus error sit voluptatem accusantium dolo remque laudantium eritatis.</p><a class="btn-pill" href="#">Read More</a></div></article>
    <article class="article-card"><div class="ph" role="img" aria-label="Photo of a calculator, wallet and clipboard" style="background:linear-gradient(135deg,#3e2b22,#d6d6d3 50%,#9a9a98)"></div><div class="card-body"><div class="date">Feb 22, 2022</div><h3 class="card-title">There are many variations of passages of Lorem Ipsum available</h3><p class="card-text">Sed ut perspiciatis unde omnis iste natus error sit voluptatem accusantium dolo remque laudantium eritatis.</p><a class="btn-pill" href="#">Read More</a></div></article>
    <article class="article-card"><div class="ph" role="img" aria-label="Photo of a hand signing papers" style="background:linear-gradient(135deg,#7c8088,#dcdcdc 55%,#f2f2f2)"></div><div class="card-body"><div class="date">Feb 22, 2022</div><h3 class="card-title">There are many variations of passages of Lorem Ipsum available</h3><p class="card-text">Sed ut perspiciatis unde omnis iste natus error sit voluptatem accusantium dolo remque laudantium eritatis.</p><a class="btn-pill" href="#">Read More</a></div></article>
    <article class="article-card"><div class="ph" role="img" aria-label="Illustration of open hands with insurance network icons" style="background:radial-gradient(circle at 75% 60%,#2f5f86,#0d1f35 70%)"></div><div class="card-body"><div class="date">Feb 22, 2022</div><h3 class="card-title">There are many variations of passages of Lorem Ipsum available</h3><p class="card-text">Sed ut perspiciatis unde omnis iste natus error sit voluptatem accusantium dolo remque laudantium eritatis.</p><a class="btn-pill" href="#">Read More</a></div></article>
    <article class="article-card"><div class="ph" role="img" aria-label="Illustration of insurance icons above a laptop" style="background:linear-gradient(135deg,#3b4a5c,#8fa2b5 50%,#2a3542)"></div><div class="card-body"><div class="date">Feb 22, 2022</div><h3 class="card-title">There are many variations of passages of Lorem Ipsum available</h3><p class="card-text">Sed ut perspiciatis unde omnis iste natus error sit voluptatem accusantium dolo remque laudantium eritatis.</p><a class="btn-pill" href="#">Read More</a></div></article>
    <article class="article-card"><div class="ph" role="img" aria-label="Photo of an advisor writing next to a calculator" style="background:linear-gradient(135deg,#cfd6e0,#6d7585 55%,#e3e5e8)"></div><div class="card-body"><div class="date">Feb 22, 2022</div><h3 class="card-title">There are many variations of passages of Lorem Ipsum available</h3><p class="card-text">Sed ut perspiciatis unde omnis iste natus error sit voluptatem accusantium dolo remque laudantium eritatis.</p><a class="btn-pill" href="#">Read More</a></div></article>
    <article class="article-card"><div class="ph" role="img" aria-label="Photo of clients shaking hands with an agent" style="background:linear-gradient(120deg,#c8bda9,#6b5e52 50%,#2c3448)"></div><div class="card-body"><div class="date">Feb 22, 2022</div><h3 class="card-title">There are many variations of passages of Lorem Ipsum available</h3><p class="card-text">Sed ut perspiciatis unde omnis iste natus error sit voluptatem accusantium dolo remque laudantium eritatis.</p><a class="btn-pill" href="#">Read More</a></div></article>
    <article class="article-card"><div class="ph" role="img" aria-label="Illustration of insurance categories on hexagons" style="background:linear-gradient(135deg,#2e4a6e,#6d8fb6 50%,#a9bcd3)"></div><div class="card-body"><div class="date">Feb 22, 2022</div><h3 class="card-title">There are many variations of passages of Lorem Ipsum available</h3><p class="card-text">Sed ut perspiciatis unde omnis iste natus error sit voluptatem accusantium dolo remque laudantium eritatis.</p><a class="btn-pill" href="#">Read More</a></div></article>
    <article class="article-card"><div class="ph" role="img" aria-label="Photo of a man with an umbrella overlooking a city" style="background:linear-gradient(180deg,#e6d2cc,#c7c9cc 50%,#9aa3ad)"></div><div class="card-body"><div class="date">Feb 22, 2022</div><h3 class="card-title">There are many variations of passages of Lorem Ipsum available</h3><p class="card-text">Sed ut perspiciatis unde omnis iste natus error sit voluptatem accusantium dolo remque laudantium eritatis.</p><a class="btn-pill" href="#">Read More</a></div></article>
  </div>
</section>

<section class="newsletter">
  <h2>SUBSCRIBE NEWSLETTER</h2>
  <p>Sed ut perspiciatis unde omnis iste natus error sit voluptatem accusantium dolo remque laudantium eritatis.</p>
  <div class="nl-form">
    <svg width="14" height="10" viewBox="0 0 14 10"><rect width="14" height="10" fill="#2d6a9b"/><path d="M0 0l7 5 7-5" fill="none" stroke="#fff" stroke-width="1.2"/></svg>
    Email Address
    <a class="btn" href="#">SUBSCRIBE</a>
  </div>
</section>

<section class="blog">
  <h2 class="section-title">Latest Blog</h2>
  <div class="wrap blog-row">
    <article class="blog-main"><div class="ph" role="img" aria-label="Photo of a team discussing papers at a desk" style="background:linear-gradient(120deg,#5a4a40,#b5a595 45%,#dcd3c6 75%,#8b8f94)"></div><h3>Lorem ipsum dolor sit amet, consectetur<br>adipiscing elit, sed do eiusmod</h3><p class="card-text">Sed ut perspiciatis unde omnis iste natus error sit voluptatem accusantium dolo remque laudantium eritatis tempor incididunt ut labore et dolore magna aliqua. Ut enim ad.</p><a class="btn-pill" href="#">Read More</a></article>
    <article class="blog-small"><div class="ph" role="img" aria-label="Photo of a handshake over a desk" style="background:linear-gradient(135deg,#1f3350,#8aa0b8 55%,#e2e6eb)"></div><h3>Lorem ipsum dolor sit amet, consectetur&nbsp; adipiscing elit, sed do eiusmod</h3><p class="card-text">Sed ut perspiciatis unde omnis iste natus error sit voluptatem accus antium dolo remque laudantium eritatis tempor incididunt ut labore et dolore magna aliqua. Ut enim ad. Duis aute irure dolor in repre henderit in voluptate velit cillum dolore eu fugiat nulla.</p><a class="btn-pill" href="#">Read More</a></article>
    <article class="blog-small"><div class="ph" role="img" aria-label="Photo of a health insurance claim form" style="background:linear-gradient(135deg,#1f5a63,#5ea3a8 55%,#a8d0cf)"></div><h3>Lorem ipsum dolor sit amet, consectetur&nbsp; adipiscing elit, sed do eiusmod</h3><p class="card-text">Sed ut perspiciatis unde omnis iste natus error sit voluptatem accus antium dolo remque laudantium eritatis tempor incididunt ut labore et dolore magna aliqua. Ut enim ad. Duis aute irure dolor in repre henderit in voluptate velit cillum dolore eu fugiat nulla.</p><a class="btn-pill" href="#">Read More</a></article>
  </div>
</section>

<footer class="site-footer">
  <div class="brand">
    <div class="brand-square"></div>
    <div><div class="brand-name">Kornfeldtakt</div><div class="brand-tag">Stets eigenständig, nie beliebig</div></div>
  </div>
  <div class="follow">Follow us <span class="icon" aria-label="Social network"></span><span class="icon" aria-label="Social network"></span><span class="icon" aria-label="Video channel"></span></div>
  <nav class="foot-nav"><a href="#">Home</a><a href="#">About Us</a><a href="#">Blog</a><a href="#">Articles</a><a href="#">Contact</a></nav>
  <div class="foot-rule"></div>
  <div class="copyright">Copyright © 2022 All Rights Reserved</div>
  <div class="powered">Powered by <span class="mark"></span><span class="name">oth<br>ostwind-tauschhalle.de</span></div>
</footer>

</body>
</html>
```